Resturant needs packaging design for cones "take away"

We need a design for the packaging of "take-away cones". we serve fries or shrimps in the salted cones. attached are 2 pictures for reference. currently we are using 2 plastic cups to cover both sides of the cone and stickers to attach them to each other.

our requirements are:
- cost effective in terms of materials for production (preferably cardboard or transperant)
- moderately traps heat (covered from both sides), like a box
- not time consuming during order dispatch

Requirements
Should not have
• pictures & bold designs. needs to be simple

```html
<!DOCTYPE html>
<html lang="en">
<head>
<meta charset="utf-8">
<title>Take-away cone box dielines</title>
<link rel="stylesheet" href="https://fonts.googleapis.com/css2?family=Roboto&display=swap">
<style>
  :root {
    --page: #ffffff;
    --cone-orange: #f7962f;
    --cone-orange-deep: #ef8a22;
    --lid-blue: #e1f2fb;
    --fold-line: #a9d6ec;
    --cut-hole: #ffffff;
  }
  html, body {
    margin: 0;
    padding: 0;
    width: 1200px;
    height: 952px;
    overflow: hidden;
    background: var(--page);
    font-family: "Roboto", sans-serif;
  }
  .dieline-sheet {
    display: block;
    width: 1200px;
    height: 952px;
  }
  .cone-net .panel { fill: var(--cone-orange); }
  .cone-net .fold { stroke: var(--fold-line); stroke-width: 1; fill: none; }
  .cone-net .window { fill: var(--cut-hole); }
  .lid-net .panel { fill: var(--lid-blue); stroke: var(--fold-line); stroke-width: 1.2; }
</style>
</head>
<body>
<svg class="dieline-sheet" viewBox="0 0 1500 1190" preserveAspectRatio="none" xmlns="http://www.w3.org/2000/svg">

  <!-- Base box net, waffle cone texture -->
  <g class="cone-net" role="img" aria-label="Base box dieline printed with a waffle cone texture">
    <!-- vertical strip -->
    <rect class="panel" x="321" y="98" width="162" height="954"/>
    <polygon class="panel" points="321,1052 483,1052 452,1150 352,1150"/>
    <!-- left side -->
    <rect class="panel" x="50" y="600" width="271" height="163"/>
    <polygon class="panel" points="50,522 288,522 321,600 50,600"/>
    <polygon class="panel" points="50,763 321,763 288,843 50,843"/>
    <!-- right side -->
    <rect class="panel" x="483" y="600" width="432" height="163"/>
    <polygon class="panel" points="515,522 915,522 915,600 483,600"/>
    <polygon class="panel" points="483,763 915,763 915,843 515,843"/>
    <!-- glue tab, symmetric about the panel centre -->
    <polygon class="panel" points="915,604 938,611 960,620 960,744 938,753 915,760"/>
    <!-- window -->
    <circle class="window" cx="834" cy="682" r="65"/>
    <!-- fold lines -->
    <line class="fold" x1="321" y1="98" x2="321" y2="1052"/>
    <line class="fold" x1="483" y1="98" x2="483" y2="1052"/>
    <line class="fold" x1="321" y1="312" x2="483" y2="312"/>
    <line class="fold" x1="321" y1="1052" x2="483" y2="1052"/>
    <line class="fold" x1="50" y1="600" x2="915" y2="600"/>
    <line class="fold" x1="50" y1="763" x2="915" y2="763"/>
    <line class="fold" x1="753" y1="522" x2="753" y2="843"/>
    <line class="fold" x1="915" y1="604" x2="915" y2="760"/>
  </g>

  <!-- Lid net -->
  <g class="lid-net" aria-label="Lid box dieline">
    <rect class="panel" x="1061" y="38" width="167" height="110"/>
    <rect class="panel" x="1059" y="148" width="171" height="112"/>
    <rect class="panel" x="1059" y="260" width="171" height="170"/>
    <rect class="panel" x="1059" y="430" width="171" height="111"/>
    <rect class="panel" x="1061" y="541" width="167" height="111"/>
    <rect class="panel" x="838" y="260" width="110" height="170"/>
    <rect class="panel" x="948" y="260" width="111" height="170"/>
    <rect class="panel" x="1230" y="260" width="110" height="170"/>
    <rect class="panel" x="1340" y="260" width="110" height="170"/>
    <polygon class="panel" points="948,168 1038,168 1049,252 1059,260 948,260"/>
    <polygon class="panel" points="1251,168 1340,168 1340,260 1230,260 1240,252"/>
    <polygon class="panel" points="948,430 1059,430 1049,437 1038,522 948,522"/>
    <polygon class="panel" points="1230,430 1340,430 1340,522 1251,522 1240,437"/>
  </g>
</svg>
</body>
</html>
```